Career Counsellor needs vibrant, professional flyer to promote inspiring new webinar

I need a flyer design, A5, double sided. I am a Career Counsellor who helps professionals create fulfilling and inspiring careers and am running a free webinar to promote my program.

I want a design which is simple, elegant and professional with the copy as below. I like dark backgrounds in general (also my name is Frost!!)
I have attached my logo, profile photo and a couple of stock photos to provide an ideal of look/feel (but you can use different stock images if you find something better).

My brand colours are:
Primary - Teal 208FA0
Highlight - Salmon F3745D
with Grey or Frost.

Copy:

(Headline)
Figuring out your next career move is easier than you think...

(webinar details)
FREE WEBINAR
"Ways to Find Direction and Build the Right Working Life for You without losing Years or Savings"
Weds 3rd Oct 7.30pm (AWST Perth)
Register here: https://lnkhop.example/7wQzRtd

(my profile)
As a Career Counsellor with 14 years of mining industry experience, I’m passionate about helping professionals get inspired by their careers.

(testimonials)
"Maren is amazing. I am so excited to now have a direction. I have finally found that spark again."
- Oriana Pexley -

"Maren steered me carefully and faithfully resulting in concrete outcomes with razor sharp clarity for me about how to proceed."
- Judith Kemble -

Target Market(s)

My target audience are mainly professional women, but also men, aged 35-45.

Font styles to use
Sans Serif
Other font styles liked:
• Logo is montserrat extra light

Requirements
Must have
• Copy provided plus profile picture and logo.
• Stylish, creative but simple design.

```html
<!DOCTYPE html>
<html lang="en">
<head>
<meta charset="utf-8">
<title>Maren Frost – Webinar Flyer</title>
<link rel="stylesheet" href="https://fonts.googleapis.com/css2?family=Archivo+Black&family=Arimo:ital,wght@0,400;1,400;1,700&family=Montserrat:wght@200;400;500&display=swap">
<style>
  :root {
    --teal: #208fa0;
    --teal-deep: #0f7686;
    --salmon: #f3745d;
    --black: #050505;
    --ink: #1b1b1b;
    --white: #ffffff;
    --stage: #7a5436;
    --bubble: rgba(20, 20, 20, 0.82);
  }
  * { margin: 0; padding: 0; box-sizing: border-box; }
  html, body { width: 1200px; height: 809px; overflow: hidden; }
  body { background: var(--stage); position: relative; font-family: "Arimo", Arial, sans-serif; }

  .flyer {
    position: absolute;
    top: 82px;
    width: 452px;
    height: 644px;
    overflow: hidden;
    box-shadow: 0 6px 18px rgba(0,0,0,0.45);
  }
  .flyer--front { left: 120px; background: var(--black); }
  .flyer--back { left: 630px; }

  .front-shapes { position: absolute; inset: 0; }

  .headline {
    position: absolute; left: 40px; top: 44px;
    color: var(--white);
    font: italic 700 24px/26px "Arimo", Arial, sans-serif;
  }

  .webinar-disc {
    position: absolute; left: 80px; top: 210px;
    width: 304px; height: 304px; border-radius: 50%;
    background: var(--salmon);
  }
  .webinar-icon { position: absolute; left: 192px; top: 238px; }
  .webinar-title {
    position: absolute; left: 0; width: 452px; top: 292px; text-align: center;
    font: 29px/1 "Archivo Black", sans-serif; color: var(--black); letter-spacing: 0.5px;
    padding-left: 16px;
  }
  .webinar-topic {
    position: absolute; left: 82px; width: 300px; top: 334px; text-align: center;
    font: italic 400 18px/22px "Arimo", Arial, sans-serif; color: var(--black);
  }
  .webinar-date {
    position: absolute; left: 82px; width: 300px; top: 414px; text-align: center;
    font: 400 14.5px/18px "Arimo", Arial, sans-serif; color: var(--black);
  }
  .register-pill {
    position: absolute; left: 68px; top: 460px; width: 314px; height: 25px;
    border-radius: 13px; background: var(--teal);
    color: var(--white); font: 400 12.5px/25px "Arimo", Arial, sans-serif;
    text-align: center; letter-spacing: 0.2px;
  }

  .brand { position: absolute; font-family: "Montserrat", sans-serif; }
  .brand-dot { position: absolute; border-radius: 50%; background: var(--salmon); }
  .brand-name { position: absolute; white-space: nowrap; font-weight: 200; color: var(--white); line-height: 1; }
  .brand-tagline { position: absolute; white-space: nowrap; font-weight: 500; color: var(--white); }

  .front-brand .brand-dot { left: 72px; top: 538px; width: 40px; height: 40px; }
  .front-brand .brand-name { left: 120px; top: 527px; font-size: 44px; }
  .front-brand .brand-tagline { left: 120px; top: 580px; font-size: 11.5px; letter-spacing: 3.6px; }

  .web-band {
    position: absolute; left: 0; width: 100%;
    font-family: "Montserrat", sans-serif; text-align: center; white-space: nowrap;
  }
  .front-web { top: 619px; height: 25px; background: var(--salmon); color: var(--ink);
    font-size: 14px; line-height: 25px; letter-spacing: 11px; font-weight: 400; }

  .portrait-scene {
    position: absolute; inset: 0;
    background: linear-gradient(180deg, #aeb0a6 0%, #9c9786 30%, #7c7a6c 48%, #5d7466 62%, #1f6f6b 80%, #0e5d60 100%);
  }
  .profile-bubble {
    position: absolute; left: 26px; top: 220px; width: 400px; height: 114px;
    background: var(--bubble); border-radius: 8px;
    color: var(--white); text-align: center;
    font: 400 17px/22px "Arimo", Arial, sans-serif;
    padding-top: 15px;
  }
  .bubble-tail { position: absolute; left: 316px; top: 186px; }

  .testimonial {
    position: absolute; top: 390px; width: 188px; height: 68px;
    background: var(--white); border-radius: 2px;
    box-shadow: 0 1px 3px rgba(0,0,0,0.3);
    font: 400 8.4px/11px "Arimo", Arial, sans-serif; color: #333;
    padding: 28px 6px 0 10px;
  }
  .testimonial::after {
    content: ""; position: absolute; right: 14px; bottom: -6px;
    border-left: 5px solid transparent; border-right: 5px solid transparent;
    border-top: 6px solid var(--white);
  }
  .testimonial--one { left: 30px; }
  .testimonial--two { left: 234px; }
  .testimonial-quote { position: absolute; left: 5px; top: 25px; font: 700 11px/1 "Arimo", serif; }
  .avatar {
    position: absolute; left: 12px; top: -12px; width: 40px; height: 40px; border-radius: 50%;
    border: 2px solid var(--white);
    background: radial-gradient(circle at 50% 40%, #b7a393, #5f6f7b);
  }
  .testimonial-name {
    position: absolute; top: 468px; width: 190px; text-align: right;
    font: italic 400 8.5px/1 "Arimo", Arial, sans-serif; color: var(--ink);
  }
  .name--one { left: 23px; }
  .name--two { left: 228px; }

  .back-brand .brand-dot { left: 44px; top: 520px; width: 46px; height: 46px; }
  .back-brand .brand-name { left: 110px; top: 511px; font-size: 50px; }
  .back-brand .brand-tagline { left: 110px; top: 568px; font-size: 13px; letter-spacing: 3.8px; }

  .back-web { top: 596px; height: 32px; background: var(--black); color: var(--salmon);
    font-size: 18px; line-height: 32px; letter-spacing: 9px; font-weight: 500; }
  .back-foot { position: absolute; left: 0; top: 628px; width: 100%; height: 16px; background: var(--teal-deep); }
</style>
</head>
<body>

<section class="flyer flyer--front">
  <svg class="front-shapes" width="452" height="644" viewBox="0 0 452 644">
    <path d="M0 0 H452 V330 C300 330 130 290 0 206 Z" fill="var(--teal)"/>
    <path d="M300 0 H452 V330 C400 331 350 327 300 320 C280 270 265 200 268 140 C272 80 285 30 300 0 Z"
          fill="#c8a286" role="img" aria-label="Photo of a woman in sunglasses looking upward"/>
  </svg>

  <h1 class="headline">Figuring out<br>your next<br>career move<br>is easier than<br>you think...</h1>

  <div class="webinar-disc"></div>
  <svg class="webinar-icon" width="64" height="52" viewBox="0 0 64 52" aria-hidden="true">
    <rect x="2" y="2" width="60" height="38" rx="3" fill="none" stroke="var(--black)" stroke-width="4"/>
    <circle cx="32" cy="15" r="5" fill="var(--black)"/>
    <path d="M22 32 C22 24 42 24 42 32 Z" fill="var(--black)"/>
    <rect x="28" y="40" width="8" height="6" fill="var(--black)"/>
    <rect x="20" y="46" width="24" height="4" fill="var(--black)"/>
  </svg>
  <h2 class="webinar-title">FREE WEBINAR</h2>
  <p class="webinar-topic">Ways to Find Direction and Build the Right Working Life for You without losing Years or Savings</p>
  <p class="webinar-date">WEDNESDAY 3RD OCT 7.30PM<br>(AWST PERTH)</p>
  <p class="register-pill">REGISTER HERE: HTTPS://LNKHOP.EXAMPLE/7WQZRTD</p>

  <div class="brand front-brand">
    <span class="brand-dot"></span>
    <span class="brand-name">Maren Frost</span>
    <span class="brand-tagline">STRATEGIC CAREER PLANNING</span>
  </div>

  <p class="web-band front-web">WWW.MARENFROST.COM</p>
</section>

<section class="flyer flyer--back">
  <div class="portrait-scene" role="img" aria-label="Portrait of the career counsellor smiling beside a eucalyptus trunk, with grass in the foreground"></div>

  <svg class="bubble-tail" width="40" height="36" viewBox="0 0 40 36" aria-hidden="true">
    <path d="M0 0 L40 34 H0 Z" fill="var(--bubble)"/>
  </svg>
  <p class="profile-bubble">As a Career Counsellor with 14 years<br>of mining industry experience, I’m passionate<br>about helping professionals get inspired<br>by their careers.</p>

  <blockquote class="testimonial testimonial--one">
    <span class="avatar" role="img" aria-label="Client headshot"></span>
    <span class="testimonial-quote">“</span>
    Maren is amazing. I am so excited to now have a direction. I have finally found that spark again.
  </blockquote>
  <p class="testimonial-name name--one">Oriana Pexley</p>

  <blockquote class="testimonial testimonial--two">
    <span class="avatar" role="img" aria-label="Client headshot"></span>
    <span class="testimonial-quote">“</span>
    Maren steered me carefully and faithfully resulting in concrete outcomes with razor sharp clarity for me about how to proceed.
  </blockquote>
  <p class="testimonial-name name--two">Judith Kemble</p>

  <div class="brand back-brand">
    <span class="brand-dot"></span>
    <span class="brand-name">Maren Frost</span>
    <span class="brand-tagline">STRATEGIC CAREER PLANNING</span>
  </div>

  <p class="web-band back-web">WWW.MARENFROST.COM</p>
  <div class="back-foot"></div>
</section>

</body>
</html>
```